Finiding oppertunites in Real Estate 6.15.20

size of ad 7” x 9.6”
1-I like the ad to stand out and attract people's attention.
2-you should be able to see the text of the ad clearly .. see the attachment anything in yellow is instructions.
3-the list of topics should not be the main part of the ad
4-if you decide you want a picture or vector of a person .. (you decide)
then it should be a white male about 25-30 years old wearing a solid white or blue shirt and not long hair.
5-leave 1 inch for footer
see attachment
Good luck

Target Market(s)

potential male students 25-35 years of age

Industry/Entity Type

Education

Requirements
Must have
• will stand out and people would want to see it.
should be able to read the words of ad
Nice to have
• how to make money in real estate on one line

```html
<!DOCTYPE html>
<html lang="en">
<head>
<meta charset="utf-8">
<title>Real Estate Career Course Flyer</title>
<link href="https://fonts.googleapis.com/css2?family=Bebas+Neue&family=Open+Sans:wght@400;600;700&display=swap" rel="stylesheet">
<style>
  :root {
    --page-bg: #e6e6e6;
    --navy: #10131c;
    --blue-deep: #1d3f86;
    --blue-mid: #2a5bb4;
    --white: #ffffff;
    --list-text: #dce6f7;
    --photo-sky: #8e9bb8;
    --photo-house: #6d6f7a;
    --photo-lawn: #4f6a3a;
    --shirt: #b8cdea;
    --ink: #111111;
  }
  * { box-sizing: border-box; margin: 0; padding: 0; }
  html, body { width: 1105px; height: 1200px; overflow: hidden; background: var(--page-bg); }
  .flyer {
    position: absolute; left: 201px; top: 119px;
    width: 702px; height: 962px;
    background: var(--white); overflow: hidden;
    box-shadow: 0 6px 14px rgba(0,0,0,.25);
  }
  .flyer-shapes { position: absolute; inset: 0; }
  .title-block {
    position: absolute; left: 36px; top: 0; width: 231px; height: 175px;
    background: var(--navy); color: var(--white);
    font-family: "Bebas Neue", sans-serif; font-size: 38px; line-height: 40px;
    text-align: center; padding-top: 60px; letter-spacing: .5px;
  }
  .headline {
    position: absolute; left: 40px; top: 200px;
    font-family: "Bebas Neue", sans-serif; font-size: 66px; line-height: 63px;
    color: var(--white); text-shadow: 0 2px 6px rgba(0,0,0,.35);
  }
  .session-badge {
    position: absolute; left: 52px; top: 407px; width: 180px; height: 180px;
    border-radius: 50%; background: rgba(255,255,255,.3);
  }
  .session-badge__disc {
    position: absolute; left: 10px; top: 10px; width: 160px; height: 160px;
    border-radius: 50%; background: var(--ink); color: var(--white);
    display: flex; flex-direction: column; align-items: center; justify-content: center;
    transform: rotate(-15deg);
  }
  .session-badge__title { font-family: "Bebas Neue", sans-serif; font-size: 31px; line-height: 28px; text-align: center; }
  .session-badge__note { font-family: "Open Sans", sans-serif; font-size: 11px; line-height: 14px; text-align: center; margin-top: 8px; }
  .offer {
    position: absolute; left: 62px; right: 0; top: 595px;
    text-align: center; color: var(--white);
  }
  .offer__heading { font-family: "Bebas Neue", sans-serif; font-size: 38px; line-height: 40px; text-shadow: 0 2px 4px rgba(0,0,0,.3); }
  .offer__lead {
    font-family: "Open Sans", sans-serif; font-weight: 600; font-size: 16.5px;
    line-height: 29px; margin-top: 19px; text-transform: uppercase;
  }
  .topics-heading {
    position: absolute; left: 116px; width: 554px; top: 738px;
    display: flex; align-items: center; gap: 10px;
    font-family: "Bebas Neue", sans-serif; font-size: 27px; color: var(--white);
    white-space: nowrap;
  }
  .topics-heading::before, .topics-heading::after {
    content: ""; flex: 1; height: 1px; background: rgba(255,255,255,.7);
  }
  .topic-list {
    position: absolute; list-style: none;
    font-family: "Open Sans", sans-serif; font-size: 13px; line-height: 17px;
    letter-spacing: 1px; color: var(--list-text);
  }
  .topic-list li::before { content: "•"; margin-right: 8px; }
  .topic-list--one { left: 116px; top: 778px; }
  .topic-list--two { left: 294px; top: 775px; }
  .topic-list--three { left: 519px; top: 775px; }
  .contact-bar {
    position: absolute; left: 100px; top: 897px; width: 578px; height: 41px;
    background: var(--white); border: 2px solid var(--blue-mid); border-radius: 21px;
    box-shadow: 0 4px 8px rgba(0,0,0,.35);
    display: flex; align-items: center; justify-content: center;
    font-family: "Open Sans", sans-serif; font-weight: 600; font-size: 18px; color: var(--ink);
  }
  .contact-bar__phone { display: flex; align-items: center; gap: 8px; }
  .contact-bar__divider { width: 2px; height: 24px; background: var(--ink); margin: 0 18px; }
</style>
</head>
<body>
<div class="flyer">
  <svg class="flyer-shapes" width="702" height="962" viewBox="0 0 702 962">
    <defs>
      <linearGradient id="photoTone" x1="0" y1="0" x2="0" y2="1">
        <stop offset="0" stop-color="var(--photo-sky)"/>
        <stop offset=".55" stop-color="var(--photo-house)"/>
        <stop offset="1" stop-color="var(--photo-lawn)"/>
      </linearGradient>
      <radialGradient id="blueField" cx=".45" cy=".3" r=".8">
        <stop offset="0" stop-color="var(--blue-mid)"/>
        <stop offset="1" stop-color="var(--blue-deep)"/>
      </radialGradient>
    </defs>
    <polygon role="img" aria-label="Photo of a large suburban house at dusk with a green lawn"
      points="0,145 702,58 702,488 62,562 0,528" fill="url(#photoTone)"/>
    <path role="img" aria-label="Photo of a smiling young businessman in a light blue shirt and striped tie, arms crossed"
      d="M450,20 Q515,0 575,30 Q590,120 560,190 Q640,205 680,250 Q702,330 690,480 L350,525 Q335,330 370,240 Q420,205 470,190 Q440,120 450,20 Z"
      fill="var(--shirt)"/>
    <polygon points="0,528 62,562 62,962 0,962" fill="var(--navy)"/>
    <polygon points="62,577 702,500 702,962 62,962" fill="url(#blueField)"/>
  </svg>

  <div class="title-block">Real Estate<br>Career Course</div>

  <h1 class="headline">How to make<br>money in<br>real estate?</h1>

  <div class="session-badge">
    <div class="session-badge__disc">
      <div class="session-badge__title">Remote<br>Sessions</div>
      <div class="session-badge__note">12 session course<br>Classes starting June 16</div>
    </div>
  </div>

  <div class="offer">
    <h2 class="offer__heading">Finiding oppertunites in real estate!</h2>
    <p class="offer__lead">For those who have started or would like to go into real estate<br>an investment in knowledge opens up untold opportunities</p>
  </div>

  <h3 class="topics-heading">A partial listing of topics</h3>

  <ul class="topic-list topic-list--one">
    <li>Single-family</li><li>Multifamily</li><li>Management</li><li>Real Estate Concepts</li><li>Real Estate law</li>
  </ul>
  <ul class="topic-list topic-list--two">
    <li>Investment properties</li><li>Foreclosures</li><li>Rehab</li><li>Foreclosures</li><li>Short sales</li>
  </ul>
  <ul class="topic-list topic-list--three">
    <li>Development</li><li>Finical modeling</li><li>HUD properties</li><li>Due Diligence</li>
  </ul>

  <div class="contact-bar">
    <span class="contact-bar__phone">CALL US
      <svg width="20" height="20" viewBox="0 0 20 20" aria-hidden="true">
        <circle cx="10" cy="10" r="8.5" fill="none" stroke="currentColor" stroke-width="1.8"/>
        <path d="M7 5.5 L8.6 5.5 L9.3 8 L8.2 8.9 Q9.2 11 11.1 11.9 L12 10.8 L14.5 11.5 L14.5 13 Q14 14.5 12.3 14.3 Q6.5 13 5.7 7.5 Q5.6 5.8 7 5.5 Z" fill="currentColor"/>
      </svg>
      012 555 0147</span>
    <span class="contact-bar__divider"></span>
    <span class="contact-bar__web">WWW.ESTATEPATHCOURSE.COM</span>
  </div>
</div>
</body>
</html>
```